Scent Marketing Solutions by Vellorant

We need to create 12 page brochure (including the cover and back page) for our Scent Marketing line of products.

The brochure size is 18 cm x 18 cm.

Our competitors are www.breeze-nimbo.example and www.odaflux.example
Updates

Hi Designers, 

The budget for this project has been increased to $300. This is a 12 page brochure of size 18cm x 18cm.

Thank you.

Hi all designers,

I uploaded a new brochure draft with the write up in pdf.
I understand that some of you could not open the original file in powerpoint.

Thank you.

Hi Designers,

I added the brochure write up in Word and PDF format. I understand some of you have troubles with it in the earlier files uploaded.

Thank you.

Target Market(s)

B2B audience, such as visual merchandisers of retail brands, hotel managers, real estate property managers etc.

Industry/Entity Type

Marketing

Requirements
Must have
• Our corporate identity uses a lot of white, hence this must be reflected in the brochure.
Our products are high-tech and environmentally friendly, so this must again be reflected in the design.
We want to make the brochure attractive and easy to read, hence would like to allocate more space for photos and pictures and keep the brochure as spacious as possible.
Nice to have
• Since the product is related to the air (it scents the air), we would like to have a design feature that reflects this and is repeated throughout the brochure. It can be a pattern or logo.
Should not have
• Avoid using a lot of bright colors

```html
<!DOCTYPE html>
<html lang="en">
<head>
<meta charset="utf-8">
<title>Vellorant – Scent Marketing Services</title>
<link href="https://fonts.googleapis.com/css2?family=Crimson+Text:wght@400;700&family=Righteous&display=swap" rel="stylesheet">
<style>
  :root {
    --paper: #ffffff;
    --mist: #e6e6e6;
    --photo-light: #f3f3f3;
    --photo-mid: #dcdcdc;
    --charcoal: #433f3d;
    --ink: #2b2b2b;
    --accent: #f15a24;
    --arc: #c9c9c9;
  }
  * { margin: 0; padding: 0; box-sizing: border-box; }
  html, body { width: 1200px; height: 600px; overflow: hidden; background: var(--paper); }
  .spread { position: relative; width: 1200px; height: 600px; background: var(--paper); overflow: hidden; font-family: "Crimson Text", Georgia, serif; color: var(--ink); }

  .product-photo {
    position: absolute; left: 0; top: 65px; width: 600px; height: 398px;
    background: linear-gradient(180deg, var(--photo-mid) 0%, #ececec 58%, var(--photo-light) 59%, #f7f7f7 100%);
  }
  .product-photo-focus {
    position: absolute; left: 162px; top: 15px; width: 298px; height: 298px; border-radius: 50%;
    border: 5px solid rgba(255,255,255,0.8);
    background: radial-gradient(circle at 45% 45%, #f1e3c2 0%, #d9b46a 30%, #e4e4e4 62%, #cfcfcf 100%);
  }
  .headline {
    position: absolute; left: 68px; top: 404px;
    font-family: "Righteous", "Arial Rounded MT Bold", sans-serif;
    font-size: 20.5px; font-weight: 400; letter-spacing: 0.2px; color: var(--accent); text-transform: uppercase;
    white-space: nowrap;
  }

  .service-band { position: absolute; left: 600px; top: 231px; width: 600px; height: 126px; background: var(--mist); }
  .decor { position: absolute; left: 0; top: 0; }

  .intro {
    position: absolute; left: 697px; top: 251px; width: 222px;
    font-size: 11.5px; line-height: 16px; color: var(--ink);
  }
  .service-list {
    position: absolute; left: 988px; top: 252px; width: 170px;
    list-style: none; color: var(--paper); font-weight: 700; font-size: 11.5px; line-height: 16.4px;
  }
  .service-list li { position: relative; padding-left: 16px; white-space: nowrap; }
  .service-list li::before { content: "•"; position: absolute; left: 0; }

  .call-to-action {
    position: absolute; left: 988px; top: 379px; width: 200px;
    font-size: 11.5px; line-height: 13.6px; color: var(--ink); white-space: nowrap;
  }
  .call-to-action strong { color: var(--accent); font-weight: 700; }

  .brand-name {
    position: absolute; left: 1100px; top: 54px;
    font-size: 17px; color: var(--ink); font-weight: 400;
  }
</style>
</head>
<body>
<main class="spread">
  <div class="product-photo" role="img" aria-label="Photo of small glass vials of amber and clear fragrance oils with a roll-on bottle on a white surface">
    <div class="product-photo-focus"></div>
  </div>
  <h1 class="headline">Support all your scent marketing needs</h1>

  <div class="service-band"></div>

  <svg class="decor" width="1200" height="600" viewBox="0 0 1200 600" aria-hidden="true">
    <defs>
      <clipPath id="band-clip"><rect x="940" y="231" width="260" height="126"/></clipPath>
    </defs>
    <g clip-path="url(#band-clip)">
      <circle cx="1292" cy="300" r="338" fill="var(--accent)"/>
      <circle cx="1298" cy="300" r="332" fill="var(--charcoal)"/>
    </g>
    <circle cx="1292" cy="300" r="332" fill="none" stroke="var(--arc)" stroke-width="1.2"/>
  </svg>

  <p class="intro">We make it easy and effortless to implement scent marketing into your business by providing a comprehensive range of services that include:</p>

  <ul class="service-list">
    <li>Signature scent design</li>
    <li>Scent selection</li>
    <li>Scent matching</li>
    <li>Application services</li>
    <li>Product development &amp;<br>contract manufacturing</li>
  </ul>

  <p class="call-to-action">Ready to unleash the power of scent<br>marketing for your business?<br>Email <strong>sales@vellorant.example</strong><br>or visit <strong>www.vellorant.example</strong><br>today to schedule your consultation.</p>

  <div class="brand-name">Vellorant</div>
</main>
</body>
</html>
```